TRV Business Card

Business card design for a handyman company. Want to portray a professional image and stay away from the "Mom & Pops" image that is normally associated with handyman companies.

Business

```html
<!DOCTYPE html>
<html lang="en">
<head>
<meta charset="utf-8">
<title>TRV Business Card</title>
<link rel="stylesheet" href="https://fonts.googleapis.com/css2?family=PT+Sans:wght@400;700&family=Libre+Baskerville:wght@400&display=swap">
<style>
  :root {
    --stage: #e6e4e1;
    --card-white: #ffffff;
    --card-grey: #7e8b8a;
    --navy: #1d2a57;
    --band: #d5d8da;
    --ink: #2b2b2b;
    --rule: #c9cccf;
    --on-grey: #ffffff;
  }
  * { box-sizing: border-box; margin: 0; padding: 0; }
  html, body { width: 1200px; height: 570px; overflow: hidden; }
  body {
    background: var(--stage);
    font-family: "PT Sans", Arial, sans-serif;
    position: relative;
  }
  .card {
    position: absolute;
    top: 142px;
    width: 500px;
    height: 286px;
    box-shadow: 0 6px 18px rgba(0,0,0,.18);
    overflow: hidden;
  }
  /* Front */
  .card-front { left: 60px; background: var(--card-white); }
  .front-bands { position: absolute; inset: 0; }
  .brand {
    position: absolute;
    left: 44px;
    top: 100px;
    display: flex;
    align-items: center;
    gap: 12px;
  }
  .brand-mark { width: 18px; height: 18px; background: var(--navy); }
  .brand-name {
    font-weight: 700;
    font-size: 52px;
    letter-spacing: 2px;
    color: var(--navy);
    line-height: 1;
  }
  .divider {
    position: absolute;
    left: 238px;
    top: 44px;
    width: 1px;
    height: 142px;
    background: var(--rule);
  }
  .contact {
    position: absolute;
    left: 252px;
    top: 48px;
    list-style: none;
    color: var(--ink);
    font-size: 14px;
    line-height: 21px;
  }
  .contact .address { font-size: 13px; line-height: 19px; margin-bottom: 2px; }
  .contact .phone { font-size: 16px; }
  .contact li { display: flex; align-items: center; gap: 4px; }
  .contact svg { width: 12px; height: 12px; fill: var(--navy); flex: none; }
  .person {
    position: absolute;
    right: 28px;
    top: 236px;
    font-family: "Libre Baskerville", Georgia, serif;
    font-variant: small-caps;
    font-size: 17px;
    color: var(--navy);
    letter-spacing: .5px;
  }
  /* Back */
  .card-back {
    left: 640px;
    background: var(--card-grey);
    color: var(--on-grey);
    text-align: center;
  }
  .back-brand {
    position: absolute;
    left: 0; right: 0;
    top: 50px;
    display: flex;
    justify-content: center;
    align-items: center;
    gap: 14px;
  }
  .back-brand .brand-mark { width: 20px; height: 20px; background: var(--on-grey); }
  .back-brand .brand-name { color: var(--on-grey); font-size: 62px; }
  .services {
    position: absolute;
    left: 0; right: 0;
    top: 150px;
    font-size: 15px;
    line-height: 19px;
  }
  .web {
    position: absolute;
    left: 0; right: 0;
    top: 232px;
    font-size: 14px;
    letter-spacing: .5px;
  }
</style>
</head>
<body>
  <section class="card card-front">
    <svg class="front-bands" viewBox="0 0 500 286" aria-hidden="true">
      <polygon points="0,286 0,268 190,268 226,230 500,230 500,286" fill="var(--band)"/>
      <polygon points="34,258 196,238 214,238 196,256 34,266" fill="var(--navy)"/>
      <polygon points="0,262 34,258 34,266 0,268" fill="var(--navy)"/>
    </svg>
    <div class="brand">
      <span class="brand-mark"></span>
      <span class="brand-name">TRV</span>
    </div>
    <div class="divider"></div>
    <ul class="contact">
      <li class="address">410 Harbor Lane,<br>Millbrook, KS 66000</li>
      <li class="phone"><svg viewBox="0 0 12 12"><path d="M3 1l2 2-1 1.5c.6 1.3 1.5 2.2 2.8 2.8L8.3 6l2 2-1.2 1.8C5.5 9.5 2.5 6.5 1.2 2.2z"/></svg>555-014-7004</li>
      <li class="phone"><svg viewBox="0 0 12 12"><rect x="3" y="0.5" width="6" height="11" rx="1.2"/></svg>555-016-3994</li>
      <li><svg viewBox="0 0 12 12"><path d="M1 2.5h10v7H1z M1 2.5l5 4 5-4" fill="none" stroke="var(--navy)" stroke-width="1.4"/></svg>info@trvhomeservices.com</li>
    </ul>
    <p class="person">Your Name, Title</p>
  </section>

  <section class="card card-back">
    <div class="back-brand">
      <span class="brand-mark"></span>
      <span class="brand-name">TRV</span>
    </div>
    <p class="services">
      Residential &amp; Commercial Services &nbsp;• Potential Verbage<br>
      • Home Repairs &nbsp;• Handyman Services<br>
      • Drain Cleaning &nbsp;• Carpet Cleaning
    </p>
    <p class="web">www.trvhomeservices.com</p>
  </section>
</body>
</html>
```